Business Card Design

I need a business card designed for my business.

The company name is Miles Renford Collective

It has four brands underneath it. They are:
- MR Occasions
- MR Athletic Journeys
- MRC Stewardship
- Dove Draftworks

I have attached all logo items, as well as our last business card.

I look forward to seeing your designs.

Industry/Entity Type

Business

Colors
eb1f27
0355a3

Requirements
Must have
• Our contact details as per the front page of our previous business card.

```html
<!DOCTYPE html>
<html lang="en">
<head>
<meta charset="utf-8">
<title>Miles Renford Collective – Business Card</title>
<link rel="stylesheet" href="https://fonts.googleapis.com/css2?family=Quicksand:wght@400;500;700&family=Arimo:wght@400&display=swap">
<style>
  :root {
    --page: #ffffff;
    --card-dark: #3b3b3d;
    --card-mid: #6d6e71;
    --brand-blue: #0355a3;
    --name-blue: #2f8fe0;
    --title-blue: #1f5fa8;
    --brand-red: #eb1f27;
    --text-light: #e6e6e6;
    --url-grey: #d8d8d8;
    --label: #222222;
  }
  * { margin: 0; padding: 0; box-sizing: border-box; }
  html, body {
    width: 1200px; height: 841px; overflow: hidden;
    background: var(--page);
    font-family: "Quicksand", "Arial", sans-serif;
  }
  .sheet { position: relative; width: 1200px; height: 841px; }

  .card { position: absolute; overflow: hidden; }
  .card--front { left: 40px; top: 56px; width: 526px; height: 322px; background: var(--card-dark); }
  .card--back-mid { left: 608px; top: 56px; width: 516px; height: 316px; background: var(--card-mid); }
  .card--back-dark { left: 608px; top: 436px; width: 516px; height: 316px; background: var(--card-dark); }

  .caption {
    position: absolute; font-family: "Arimo", "Arial", sans-serif;
    font-size: 19px; color: var(--label);
  }

  /* company mark */
  .mark-dot { position: absolute; border-radius: 50%; background: var(--brand-blue); }
  .company-name {
    position: absolute; color: var(--name-blue); font-weight: 700;
    text-transform: uppercase; line-height: 1; text-align: right;
  }
  .company-rule { position: absolute; height: 3px; background: var(--brand-red); }

  /* front */
  .card--front .mark-dot { left: 40px; top: 34px; width: 80px; height: 80px; }
  .card--front .company-name { left: 134px; top: 30px; font-size: 38px; letter-spacing: 1px; }
  .card--front .company-name .line2 { display: block; font-size: 26px; margin-top: 8px; }
  .card--front .company-rule { left: 134px; top: 76px; width: 210px; }

  .person { position: absolute; left: 40px; top: 164px; }
  .person-name { font-size: 21px; font-weight: 500; color: var(--name-blue); }
  .person-role { font-size: 18px; color: var(--title-blue); margin-top: 2px; }
  .contact {
    position: absolute; font-size: 17px; line-height: 24px; color: var(--text-light);
  }
  .contact--phones { left: 230px; top: 166px; }
  .contact--address { left: 40px; top: 226px; }
  .contact--web { left: 230px; top: 226px; }

  /* backs */
  .back-head .mark-dot { left: 76px; top: 18px; width: 68px; height: 68px; }
  .back-head .company-name { left: 160px; top: 16px; font-size: 32px; letter-spacing: 1px; }
  .back-head .company-name .line2 { display: block; font-size: 22px; margin-top: 6px; }
  .back-head .company-rule { left: 160px; top: 56px; width: 170px; }
  .back-url {
    position: absolute; left: 0; width: 100%; top: 92px; text-align: center;
    font-size: 22px; color: var(--url-grey); padding-left: 70px;
  }
  .band { position: absolute; left: 0; width: 100%; top: 124px; height: 10px; background: var(--brand-red); }
  .brand {
    position: absolute; width: 240px; text-align: center;
    font-weight: 700; font-size: 22px; line-height: 1.1; color: var(--name-blue);
  }
  .brand--red { color: var(--brand-red); }
  .brand--tl { left: 10px; top: 172px; }
  .brand--tr { left: 256px; top: 172px; }
  .brand--bl { left: 10px; top: 254px; }
  .brand--br { left: 256px; top: 254px; }
</style>
</head>
<body>
<main class="sheet">

  <section class="card card--front" aria-label="Card front">
    <span class="mark-dot"></span>
    <div class="company-name">Miles Renford<span class="line2">Collective</span></div>
    <div class="person">
      <p class="person-name">Miles Renford</p>
      <p class="person-role">Principal</p>
    </div>
    <p class="contact contact--phones">+61 2 5550 0142<br>+61 400 555 318</p>
    <p class="contact contact--address">PO Box 418<br>Larkfield ACT 2619<br>Australia</p>
    <p class="contact contact--web">miles@milesrenford.com.au<br>milesrenford.com.au</p>
  </section>
  <p class="caption" style="left:40px; top:392px;">Front</p>

  <section class="card card--back-mid back-head" aria-label="Card back, option 2">
    <span class="mark-dot"></span>
    <div class="company-name">Miles Renford<span class="line2">Collective</span></div>
    <p class="back-url">milesrenford.com.au</p>
    <div class="band"></div>
    <p class="brand brand--tl">MR Occasions</p>
    <p class="brand brand--tr">MR Athletic Journeys</p>
    <p class="brand brand--bl brand--red">Dove Draftworks</p>
    <p class="brand brand--br">MRC Stewardship</p>
  </section>
  <p class="caption" style="left:608px; top:388px;">Back Option 2</p>

  <section class="card card--back-dark back-head" aria-label="Card back, option 3">
    <span class="mark-dot"></span>
    <div class="company-name">Miles Renford<span class="line2">Collective</span></div>
    <p class="back-url">milesrenford.com.au</p>
    <div class="band"></div>
    <p class="brand brand--tl">MR Occasions</p>
    <p class="brand brand--tr">MR Athletic Journeys</p>
    <p class="brand brand--bl brand--red">Dove Draftworks</p>
    <p class="brand brand--br">MRC Stewardship</p>
  </section>
  <p class="caption" style="left:608px; top:766px;">Back Option 3</p>

</main>
</body>
</html>
```